Psychotherapist's business card

I need a business card design for a psychotherapist. I expect business card to have "light" design. By this I mean that it can somehow translate easiness, serenity. Maybe pastel colours can help you here. I have attached some pictures from Greece. Perhaps they can inspire you to combine colours and to achieve that "light" design.
Updates

Pls, don't use any free samples you may find on business card generators. It looks too simple, uncreative and waste of time! READ size and colour requirements! I don't want to see any shapes like rings, triangles etc.

Contact Information for Business Card

Size: 65mmX60mm

Name - Мирослав Гречихин

Психолог
+7(916)482-39-07
grechikhin.com

I suppose that thin font can look good but it's up to you

Requirements
Must have
• size requirements
Nice to have
• pastel colours
• thin font
Should not have
• black and dark colours
• lines, free design samples used from other web-sites

```html
<!DOCTYPE html>
<html lang="ru">
<head>
<meta charset="utf-8">
<title>Мирослав Гречихин — визитка</title>
<link rel="stylesheet" href="https://fonts.googleapis.com/css2?family=Didact+Gothic&display=swap">
<style>
  :root {
    --sky: #86c2e6;
    --sky-text: #4f97c6;
    --peach: #f5c27e;
    --white: #ffffff;
    --slate: #56758c;
    --mist: #d6eaf6;
  }
  * { margin: 0; padding: 0; box-sizing: border-box; }
  html, body { width: 1200px; height: 1108px; overflow: hidden; background: var(--white); }
  .card {
    position: relative;
    width: 1200px;
    height: 1108px;
    background: var(--white);
    font-family: "Didact Gothic", "Century Gothic", sans-serif;
    overflow: hidden;
  }
  .card__header { position: absolute; left: 0; top: 0; width: 1200px; height: 580px; }
  .card__name {
    position: absolute;
    left: 0; top: 150px;
    width: 100%;
    text-align: center;
    color: var(--white);
    font-size: 92px;
    line-height: 118px;
    font-weight: 400;
    letter-spacing: 1px;
  }
  .card__role {
    position: absolute;
    left: 0; top: 645px;
    width: 100%;
    text-align: center;
    color: var(--slate);
    font-size: 80px;
    line-height: 100px;
    font-weight: 400;
  }
  .contact {
    position: absolute;
    top: 822px;
    width: 600px;
    text-align: center;
    color: var(--sky-text);
  }
  .contact--phone { left: 12px; }
  .contact--web { left: 583px; }
  .contact__icon { display: block; margin: 0 auto; width: 72px; height: 72px; }
  .contact__text { display: block; margin-top: 26px; line-height: 56px; }
  .contact--phone .contact__text { font-size: 48px; }
  .contact--web .contact__text { font-size: 43px; }
  .card__footer-band {
    position: absolute;
    left: 0; bottom: 0;
    width: 1200px; height: 10px;
    background: var(--mist);
  }
</style>
</head>
<body>
<div class="card">
  <svg class="card__header" viewBox="0 0 1200 580" aria-hidden="true">
    <path d="M0 0 H1200 V428 Q600 714 0 428 Z" fill="var(--peach)"/>
    <path d="M0 0 H1200 V420 Q600 702 0 420 Z" fill="var(--sky)"/>
  </svg>

  <h1 class="card__name">Мирослав<br>Гречихин</h1>
  <p class="card__role">Психолог</p>

  <div class="contact contact--phone">
    <svg class="contact__icon" viewBox="0 0 72 72" aria-hidden="true">
      <circle cx="36" cy="36" r="32" fill="none" stroke="var(--peach)" stroke-width="4"/>
      <path d="M25 20 l7 -2 l5 10 l-5 4 q3 8 9 11 l4 -5 l10 5 l-2 7 q-4 4 -10 2 q-14 -6 -20 -22 q-2 -6 2 -10 Z" fill="var(--peach)"/>
    </svg>
    <span class="contact__text">+7(916)482-39-07</span>
  </div>

  <div class="contact contact--web">
    <svg class="contact__icon" viewBox="0 0 72 72" aria-hidden="true">
      <circle cx="36" cy="36" r="32" fill="none" stroke="var(--peach)" stroke-width="4"/>
      <circle cx="36" cy="36" r="22" fill="var(--peach)"/>
      <g fill="none" stroke="var(--white)" stroke-width="2.5">
        <ellipse cx="36" cy="36" rx="9" ry="22"/>
        <line x1="36" y1="14" x2="36" y2="58"/>
        <line x1="14" y1="36" x2="58" y2="36"/>
        <path d="M18 26 H54 M18 46 H54"/>
      </g>
    </svg>
    <span class="contact__text">www.grechikhin.com</span>
  </div>

  <div class="card__footer-band"></div>
</div>
</body>
</html>
```